Wedding Invite Location

We had my daughter's wedding invitations printed and mailed out before realizing we forgot to put the location of the wedding on the invitation. We would like to send out a postcard with the location to all who received an invitation

The pertinent information:

Bethany Morrow and Gregory Sadowin

Grace Fellowship Chapel
24650 Melbrook Rd.
St. Clair Shores, MI 48237

Reception immediately following the service on the church grounds

```html
<!DOCTYPE html>
<html lang="en">
<head>
<meta charset="utf-8">
<title>We Forgot… Wedding Location Postcard</title>
<link rel="stylesheet" href="https://fonts.googleapis.com/css2?family=Amatic+SC:wght@700&family=Josefin+Sans:wght@300;400&family=Gochi+Hand&family=Great+Vibes&family=Roboto+Condensed:wght@400&display=swap">
<style>
  :root {
    --card-white: #ffffff;
    --panel-pink: #f07d86;
    --title-pink: #e9707b;
    --banner-tint: rgba(255, 236, 238, 0.88);
    --soft-pink: #fbd0d3;
    --ghost-pink: rgba(226, 96, 108, 0.35);
    --photo-light: #ddd0d3;
    --photo-mid: #c6b6ba;
    --photo-dark: #9e8f94;
  }
  * { margin: 0; padding: 0; box-sizing: border-box; }
  html, body {
    width: 1200px;
    height: 928px;
    overflow: hidden;
    background: var(--card-white);
  }
  .postcard {
    position: relative;
    width: 1200px;
    height: 928px;
    background: var(--card-white);
    overflow: hidden;
  }
  .couple-photo {
    position: absolute;
    left: 30px;
    top: 26px;
    width: 612px;
    height: 872px;
    background:
      radial-gradient(ellipse at 40% 65%, var(--photo-light) 0%, rgba(221,208,211,0) 60%),
      linear-gradient(160deg, var(--photo-light) 0%, var(--photo-mid) 55%, var(--photo-dark) 100%);
  }
  .details-panel {
    position: absolute;
    left: 642px;
    top: 26px;
    width: 528px;
    height: 872px;
    background: var(--panel-pink);
  }
  .headline-banner {
    position: absolute;
    left: 570px;
    top: 72px;
    width: 520px;
    height: 128px;
    background: var(--banner-tint);
  }
  .headline {
    position: absolute;
    left: 604px;
    top: 78px;
    font-family: "Amatic SC", "Arial Narrow", sans-serif;
    font-weight: 700;
    font-size: 96px;
    line-height: 1.2;
    letter-spacing: 4px;
    color: var(--title-pink);
    white-space: nowrap;
  }
  .subhead {
    position: absolute;
    left: 706px;
    top: 212px;
    font-family: "Josefin Sans", sans-serif;
    font-weight: 400;
    font-size: 28px;
    letter-spacing: 2px;
    color: var(--card-white);
    white-space: nowrap;
  }
  .venue-name {
    position: absolute;
    left: 734px;
    top: 334px;
    font-family: "Gochi Hand", cursive;
    font-size: 36px;
    color: var(--card-white);
    white-space: nowrap;
  }
  .venue-street {
    position: absolute;
    left: 734px;
    top: 396px;
    font-family: "Gochi Hand", cursive;
    font-size: 46px;
    color: var(--card-white);
    white-space: nowrap;
  }
  .venue-city {
    position: absolute;
    left: 736px;
    top: 470px;
    font-family: "Josefin Sans", sans-serif;
    font-weight: 300;
    font-size: 27px;
    letter-spacing: 1px;
    color: var(--soft-pink);
    white-space: nowrap;
  }
  .names-ghost {
    position: absolute;
    left: 790px;
    top: 528px;
    font-family: "Great Vibes", cursive;
    font-size: 104px;
    line-height: 0.9;
    color: var(--ghost-pink);
    white-space: nowrap;
  }
  .couple-names {
    position: absolute;
    left: 800px;
    top: 598px;
    width: 360px;
    height: 170px;
    font-family: "Great Vibes", cursive;
    color: var(--card-white);
  }
  .bride-name {
    position: absolute;
    left: 0;
    top: 14px;
    font-size: 60px;
    white-space: nowrap;
  }
  .ampersand {
    position: absolute;
    left: 196px;
    top: -16px;
    font-size: 104px;
  }
  .groom-name {
    position: absolute;
    left: 70px;
    top: 80px;
    font-size: 60px;
    white-space: nowrap;
  }
  .reception-note {
    position: absolute;
    left: 660px;
    top: 814px;
    width: 490px;
    font-family: "Roboto Condensed", "Arial Narrow", sans-serif;
    font-size: 20px;
    line-height: 1.6;
    color: var(--card-white);
  }
</style>
</head>
<body>
  <main class="postcard">
    <div class="couple-photo" role="img" aria-label="Photo of the bride and groom seen from above, the bride tossing a bouquet of red roses into the air"></div>
    <section class="details-panel"></section>

    <div class="headline-banner"></div>
    <h1 class="headline">We Forgot...</h1>
    <p class="subhead">TO TELL YOU WHERE !!</p>

    <p class="venue-name">Grace Fellowship Chapel</p>
    <p class="venue-street">24650 Melbrook Rd.</p>
    <p class="venue-city">ST. CLAIR SHORES, MI 48237</p>

    <p class="names-ghost" aria-hidden="true">Bethany<br>Gregory</p>
    <div class="couple-names">
      <span class="bride-name">Bethany</span>
      <span class="ampersand">&amp;</span>
      <span class="groom-name">Gregory</span>
    </div>

    <p class="reception-note">Reception immediately following the service on the church grounds</p>
  </main>
</body>
</html>
```